Our brand new and excilting business, ZEPPO wares, needs a fresh, vibriant and clean website that is

We need a new website designed to sell our ZEPPO wares products to schools and fundraisers. We plan to have around 24 items with great images, add to cart and some really new and cool products. This site needs to be clean, fresh and funky, really clean lines, easy to navigate but look really fun and fresh

Target Market(s)

School fundraising. Kids

Industry/Entity Type

Business

Number of Pages Required

4 page

Colors
add136
fbee3d
fbed22
9bcb3c
f78f20

Requirements
Must have
• Fresh, fun and easy to navigate. Great shopping product page that has images of our products and add to cart
Nice to have
• Flashing image availibility
Should not have
• Must not be old and boring

```html
<!DOCTYPE html>
<html lang="en">
<head>
<meta charset="utf-8">
<title>ZEPPO wares – The school fundraising specialists</title>
<link href="https://fonts.googleapis.com/css2?family=Open+Sans:wght@400;600;700;800&family=Oswald:wght@500;600&display=swap" rel="stylesheet">
<style>
:root{
  --green:#9bcb3c;
  --green-dark:#7fae26;
  --orange:#f78f20;
  --yellow:#fbee3d;
  --ink:#2b2b2b;
  --dark:#1c1c1c;
  --footer:#333333;
  --grey:#f1f1f1;
  --mid:#8a8a8a;
  --white:#ffffff;
}
*{box-sizing:border-box;margin:0;padding:0}
html,body{width:1200px;height:3156px;overflow:hidden;background:var(--white)}
body{font-family:"Open Sans",Arial,sans-serif;color:var(--ink);position:relative}
.abs{position:absolute}

/* header */
.toplinks{right:250px;top:0;display:flex;gap:4px}
.toplinks span{background:var(--ink);color:#fff;font-size:12px;padding:7px 14px;display:block}
.cart{right:140px;top:0;width:110px;height:30px;background:var(--ink);color:#fff;font-size:13px;font-weight:700;display:flex;align-items:center;justify-content:center;gap:8px}
.logo{left:140px;top:26px}
.logo .brand{font-weight:800;font-size:46px;color:var(--green);letter-spacing:-1px;line-height:1}
.logo .tag{font-size:13px;color:var(--mid);font-weight:600;margin-top:4px}
.search{left:640px;top:70px;width:220px;height:32px;border:1px solid #ccc;border-radius:3px;font-size:12px;color:#999;padding:7px 10px}
.search svg{position:absolute;right:8px;top:8px}
.phone{left:900px;top:66px;display:flex;align-items:center;gap:8px;font-size:22px;font-weight:700;color:var(--ink)}

/* nav */
.nav{left:0;top:132px;width:1200px;height:38px;background:var(--green)}
.nav ul{list-style:none;display:flex;margin-left:140px;height:38px}
.nav li{color:#fff;font-size:13px;font-weight:600;padding:0 17px;line-height:38px;white-space:nowrap}
.nav li.active{background:var(--orange)}

/* hero */
.hero{left:0;top:170px;width:1200px;height:450px;background:radial-gradient(circle at 70% 40%,#2b2b30,#0f0f10 70%)}
.hero-person{left:140px;top:40px;width:250px;height:410px;background:linear-gradient(180deg,#3a2c2e,#1a1a1c)}
.hero-wand{left:300px;top:30px;width:280px;height:300px;background:radial-gradient(circle at 50% 50%,#d04adf,#5b1a7a 55%,transparent 72%)}
.hero-toys{left:660px;top:50px;width:400px;height:150px;background:linear-gradient(90deg,#c8283a,#e8e6ea 50%,#2a66c8)}
.hero-copy{left:580px;top:250px;width:500px;color:#fff;font-size:34px;font-weight:600;line-height:1.25;text-align:right}
.hero-dots{left:975px;top:420px;display:flex;gap:8px}
.hero-dots i{width:12px;height:12px;border-radius:50%;background:#fff;display:block}
.hero-dots i.on{background:var(--green)}

/* welcome */
.welcome{left:140px;top:660px;width:920px;text-align:center}
.welcome h1{font-family:"Oswald",Arial,sans-serif;font-weight:600;font-size:40px;color:var(--ink);display:flex;justify-content:center;align-items:baseline;gap:14px}
.welcome h1 span{font-family:"Open Sans",Arial,sans-serif;font-weight:800;color:var(--green);font-size:42px;letter-spacing:-1px}
.welcome p{margin-top:30px;font-size:12px;line-height:1.75;color:#666;text-align:left}
.btn-more{display:inline-block;margin-top:22px;background:var(--ink);color:#fff;font-size:12px;font-weight:600;padding:8px 18px;border-radius:3px}

/* products */
.products{left:0;top:960px;width:1200px;height:1160px;background:linear-gradient(180deg,#e4e4e4,#f7f7f7 8%,#ffffff 20%)}
.products h2{position:absolute;left:0;top:24px;width:1200px;text-align:center;font-family:"Oswald",Arial,sans-serif;font-weight:500;font-size:26px;letter-spacing:1px;color:var(--ink)}
.products h2 b{color:var(--orange);font-weight:500}
.tile{position:absolute;overflow:hidden;background:#111}
.tile .photo{position:absolute;inset:0}
.tile .label{position:absolute;color:#fff;white-space:nowrap}
.tile .label .name{font-size:15px;font-weight:700;text-transform:uppercase}
.tile .label .price{font-size:14px;font-weight:700;color:var(--green)}
.shop{display:inline-flex;align-items:center;gap:6px;margin-top:6px;background:var(--green);color:#fff;font-size:12px;font-weight:700;padding:5px 10px;border-radius:2px}

/* promo cards */
.card{position:absolute;top:2140px;width:300px;height:380px;background:var(--ink)}
.card .art{position:absolute;left:0;top:0;width:300px;height:290px}
.card .cap{position:absolute;left:0;top:290px;width:300px;height:90px;color:#fff;text-align:center;font-weight:800;font-size:18px;display:flex;align-items:center;justify-content:center;line-height:1.2}
.banner{position:absolute;top:2552px;width:300px;height:96px;background:var(--ink);color:#fff;display:flex;align-items:center;gap:18px;padding:0 24px;font-weight:800;font-size:17px;line-height:1.25}
.banner.light{background:#e9f2d6;color:var(--ink)}

/* footer */
.footer{left:0;top:2690px;width:1200px;height:410px;background:var(--footer);color:#ddd}
.ftitle{font-size:13px;font-weight:700;color:#fff;text-transform:uppercase}
.testimonial{left:140px;top:16px;width:300px}
.testimonial .quote{margin-top:14px;display:flex;gap:12px;font-size:11px;line-height:1.6;color:#ccc}
.testimonial .avatar{width:54px;height:54px;flex:none;background:#5a5a5a;border-radius:50%}
.offer{position:absolute;top:10px;width:196px;height:130px;color:#fff;text-align:center;padding-top:18px}
.offer .pct{font-family:"Oswald",Arial,sans-serif;font-size:44px;line-height:1;font-weight:600}
.offer .what{font-size:12px;font-weight:700;margin-top:8px;line-height:1.35;text-transform:uppercase}
.col{position:absolute;top:170px}
.col ul{list-style:none;margin-top:14px}
.col li{font-size:12px;color:#ccc;line-height:2.1;white-space:nowrap}
.col li::before{content:"›";color:var(--green);margin-right:8px}
.nl-box{display:flex;margin-top:12px}
.nl-box .field{width:220px;height:30px;background:#fff}
.nl-box .go{width:50px;height:30px;background:var(--green);color:#fff;font-size:12px;font-weight:700;text-align:center;line-height:30px}
.contact-line{display:flex;gap:10px;align-items:center;font-size:12px;color:#ccc;margin-top:10px}
.reg{left:0;top:378px;width:1200px;text-align:center;font-size:11px;color:#bbb}
.bottom{left:0;top:3100px;width:1200px;height:56px;background:#ececec;border-top:4px solid var(--green)}
.bottom .legal{position:absolute;left:140px;top:18px;font-size:11px;color:#555}
.social{position:absolute;left:544px;top:11px;display:flex;gap:8px}
.social i{width:26px;height:26px;border-radius:50%;background:#444;display:block}
</style>
</head>
<body>

<div class="abs toplinks"><span>Login | Register</span><span>Order Status</span><span>My Account</span><span>Help</span></div>
<div class="abs cart">
  <svg width="16" height="14" viewBox="0 0 16 14"><path d="M0 1h3l2 8h8l2-6H4" fill="none" stroke="#fff" stroke-width="1.6"/><circle cx="6" cy="12" r="1.3" fill="#fff"/><circle cx="12" cy="12" r="1.3" fill="#fff"/></svg>
  0 items
</div>
<div class="abs logo">
  <div class="brand">ZEPPO wares</div>
  <div class="tag">The school fundraising specialists</div>
</div>
<div class="abs search">Search…
  <svg width="14" height="14" viewBox="0 0 14 14"><circle cx="6" cy="6" r="4.5" fill="none" stroke="#888" stroke-width="1.6"/><path d="M9.5 9.5 13 13" stroke="#888" stroke-width="1.6"/></svg>
</div>
<div class="abs phone">
  <svg width="22" height="22" viewBox="0 0 24 24"><path d="M6.6 10.8a15 15 0 0 0 6.6 6.6l2.2-2.2c.3-.3.7-.4 1-.2 1.1.4 2.3.6 3.6.6.6 0 1 .4 1 1V20c0 .6-.4 1-1 1A17 17 0 0 1 3 4c0-.6.4-1 1-1h3.5c.6 0 1 .4 1 1 0 1.3.2 2.5.6 3.6.1.3 0 .7-.2 1z" fill="var(--ink)"/></svg>
  0800 555 0199
</div>

<nav class="abs nav"><ul>
  <li class="active">Home</li><li>Glow Sticks</li><li>Glow &amp; Light Up Novelties</li><li>Glowing Necklaces</li><li>Glow Bracelets</li><li>Party Supplies</li><li>Wholesalers</li><li>Contact Us</li>
</ul></nav>

<section class="abs hero">
  <div class="abs hero-person" role="img" aria-label="Photo of a smiling girl holding a glowing star wand"></div>
  <div class="abs hero-wand" role="img" aria-label="Pink light-up star wand glowing"></div>
  <div class="abs hero-toys" role="img" aria-label="Light-up novelty toys in red, white and blue"></div>
  <div class="abs hero-copy">Buy Glow Necklaces, Glow<br>Bracelets Glowsticks &amp;<br>MUCH More!</div>
  <div class="abs hero-dots"><i class="on"></i><i></i><i></i><i></i></div>
</section>

<section class="abs welcome">
  <h1>WELCOME TO <span>ZEPPO wares</span></h1>
  <p>Our shop brings bright, safe and fun glowing products to schools, clubs and charities across the country. Every item is chosen to light up discos, fetes, sports days and fundraising nights, and every order is packed with care by our friendly team. From classic glow sticks and bracelets to flashing novelties, party packs and light-up wands, we stock everything you need to make an event shine. We offer bulk pricing for schools and PTAs, fast delivery on all orders, and simple returns if anything is not quite right. Browse our range, add your favourites to the cart and get ready for a brilliant night. Need help choosing? Our team is always happy to suggest the best products for your budget and audience, so just get in touch and we will help you plan a glowing success for your next fundraiser or celebration.</p>
  <span class="btn-more">Read More ›</span>
</section>

<section class="abs products">
  <h2>GLOW <b>PRODUCTS</b></h2>

  <div class="tile" style="left:140px;top:88px;width:600px;height:352px">
    <div class="photo" role="img" aria-label="Photo of a girl holding bright glow sticks" style="background:linear-gradient(90deg,#3b2a22,#6a4a3a 35%,#2a1a4a 70%,#1a1a2a)"></div>
    <div class="label" style="left:420px;top:30px"><div class="name">Glow Sticks 6"</div><div class="price">£6.95</div><span class="shop">🛒 Shop Now</span></div>
  </div>

  <div class="tile" style="left:760px;top:88px;width:300px;height:252px">
    <div class="photo" role="img" aria-label="Photo of a child with a rainbow windmill" style="background:linear-gradient(160deg,#e6e6e6,#c9a07a 60%,#4a6ab0)"></div>
    <div class="label" style="left:16px;top:14px"><div class="name" style="color:var(--ink)">Rainbow Windmill</div><div class="price">£20.02</div><span class="shop">🛒 Shop Now</span></div>
  </div>

  <div class="tile" style="left:140px;top:460px;width:600px;height:320px">
    <div class="photo" role="img" aria-label="Photo of glow bracelets and a smiling girl in the dark" style="background:linear-gradient(90deg,#1a1030,#2a1a5a 40%,#3a2a2a 70%,#1a1a1a)"></div>
    <div class="label" style="left:30px;top:24px"><div class="name">Glow Sticks 4"</div><div class="price">£4.95</div><span class="shop">🛒 Shop Now</span></div>
  </div>

  <div class="tile" style="left:760px;top:360px;width:300px;height:420px">
    <div class="photo" role="img" aria-label="Photo of a girl wearing glow necklaces and a boxed necklace pack" style="background:linear-gradient(180deg,#f2f2f2 0%,#c89a84 40%,#2a2a3a 75%,#1a1a1a)"></div>
    <div class="label" style="left:146px;top:20px"><div class="name" style="color:var(--ink)">Glow Necklaces</div><div class="price">£29.95</div><span class="shop">🛒 Shop Now</span></div>
  </div>

  <div class="tile" style="left:140px;top:820px;width:300px;height:320px">
    <div class="photo" role="img" aria-label="Photo of a mirrorball motor and disco ball box" style="background:linear-gradient(160deg,#e86ab0,#a03080 50%,#3a1040)"></div>
    <div class="label" style="left:16px;top:16px"><div class="name">Mirrorball Motor</div><div class="price">£3.95</div><span class="shop">🛒 Shop Now</span></div>
  </div>

  <div class="tile" style="left:460px;top:820px;width:600px;height:320px">
    <div class="photo" role="img" aria-label="Photo of a spinning mirrorball and a lantern light in purple light" style="background:linear-gradient(90deg,#2a1a4a,#6a3ac0 50%,#c0a0f0 80%,#5a2a9a)"></div>
    <div class="label" style="left:20px;top:16px"><div class="name">Mirrorball Motor</div><div class="price">£3.95</div><span class="shop">🛒 Shop Now</span></div>
  </div>
</section>

<div class="card" style="left:140px">
  <div class="art" role="img" aria-label="Catalogue cover with flash novelties" style="background:linear-gradient(180deg,#3a6ad0,#f6f6f6 60%)"></div>
  <div class="cap" style="flex-direction:column;background:var(--green)"><span style="font-size:22px">2015 - 2016</span><span style="font-size:15px">NEW CATALOGUE &nbsp;⬇ DOWNLOAD</span></div>
</div>
<div class="card" style="left:450px">
  <div class="art" role="img" aria-label="Guarantee seal on a red background" style="background:radial-gradient(circle at 50% 45%,#f2c23a,#c0281e 55%,#7a1010)"></div>
  <div class="cap">REPLACE OR<br>REFUND OFFERED</div>
</div>
<div class="card" style="left:760px">
  <div class="art" role="img" aria-label="Coloured glow necklaces hanging beside a pound coin" style="background:linear-gradient(90deg,#2a2a2a,#4a7a2a 40%,#c0902a 70%,#2a2a2a)"></div>
  <div class="cap">PTA AND<br>CHARITY DISCOUNTS</div>
</div>

<div class="banner" style="left:140px">
  <svg width="44" height="30" viewBox="0 0 44 30"><rect x="1" y="4" width="26" height="18" fill="#fff"/><path d="M27 10h9l6 6v6H27z" fill="#fff"/><circle cx="9" cy="25" r="4" fill="#fff" stroke="var(--ink)" stroke-width="2"/><circle cx="34" cy="25" r="4" fill="#fff" stroke="var(--ink)" stroke-width="2"/></svg>
  <span>ENJOY EVERYDAY<br>FREE SHIPPING</span>
</div>
<div class="banner" style="left:450px">
  <svg width="36" height="30" viewBox="0 0 36 30"><rect x="2" y="2" width="32" height="26" fill="none" stroke="#fff" stroke-width="2.5"/><path d="M8 10h20M8 16h20M8 22h12" stroke="#fff" stroke-width="2"/></svg>
  <span>REQUEST A<br>FREE CATALOG</span>
</div>
<div class="banner light" style="left:760px">
  <svg width="40" height="30" viewBox="0 0 40 30"><rect x="2" y="4" width="36" height="22" rx="3" fill="var(--green)"/><path d="M20 4v22M2 15h36" stroke="#fff" stroke-width="2.5"/></svg>
  <span>E-GIFT<br>CARDS</span>
</div>

<footer class="abs footer">
  <div class="abs testimonial">
    <div class="ftitle">What our customers say</div>
    <div class="quote"><div class="avatar"></div><p>"Fantastic service and quick delivery. The children loved the glow bracelets at our summer disco and we raised more than ever before." <br><b style="color:#fff">— Sarah, PTA Chair</b></p></div>
  </div>
  <div class="offer" style="left:460px;background:#c9702a"><div class="pct">70% OFF</div><div class="what">Natural jewellery<br>and gifts</div></div>
  <div class="offer" style="left:662px;background:#5a4a3e"><div class="pct">30% OFF</div><div class="what">Wedding and<br>anniversary</div></div>
  <div class="offer" style="left:864px;background:#7a9a3a"><div class="pct">10% OFF</div><div class="what">Unique handmade<br>jewellery</div></div>

  <div class="col" style="left:140px">
    <div class="ftitle">Newsletter</div>
    <div class="nl-box"><div class="field"></div><div class="go">GO</div></div>
    <div class="ftitle" style="margin-top:30px">Contact details</div>
    <div class="contact-line"><svg width="12" height="16" viewBox="0 0 12 16"><path d="M6 0a6 6 0 0 0-6 6c0 4.5 6 10 6 10s6-5.5 6-10a6 6 0 0 0-6-6zm0 8.5A2.5 2.5 0 1 1 6 3.5a2.5 2.5 0 0 1 0 5z" fill="var(--green)"/></svg>Unit 4 Elm Court, Brookvale, Northshire NB2 4QT</div>
    <div class="contact-line"><svg width="14" height="14" viewBox="0 0 24 24"><path d="M6.6 10.8a15 15 0 0 0 6.6 6.6l2.2-2.2c.3-.3.7-.4 1-.2 1.1.4 2.3.6 3.6.6.6 0 1 .4 1 1V20c0 .6-.4 1-1 1A17 17 0 0 1 3 4c0-.6.4-1 1-1h3.5c.6 0 1 .4 1 1 0 1.3.2 2.5.6 3.6.1.3 0 .7-.2 1z" fill="var(--green)"/></svg>0800 555 0199</div>
    <div class="contact-line"><svg width="14" height="12" viewBox="0 0 14 12"><rect x="1" y="1" width="12" height="10" fill="none" stroke="var(--green)" stroke-width="1.6"/><path d="M1 1l6 5 6-5" fill="none" stroke="var(--green)" stroke-width="1.6"/></svg>hello@zeppowares.example</div>
  </div>

  <div class="col" style="left:520px">
    <div class="ftitle">Quick links</div>
    <ul><li>Home</li><li>Glow Sticks</li><li>Glow Bracelets</li><li>Glow &amp; Light Up Novelties</li><li>Glowing Necklaces</li></ul>
  </div>
  <div class="col" style="left:690px">
    <div class="ftitle">&nbsp;</div>
    <ul><li>Party Supplies</li><li>Wholesalers</li><li>Contact Us</li></ul>
  </div>
  <div class="col" style="left:860px">
    <div class="ftitle">Help and information</div>
    <ul><li>Delivery Information</li><li>Customer Service Area</li><li>Our Customer Comments</li><li>Glowsticks: How To &amp; FAQs</li><li>Quality and Safety Information</li></ul>
  </div>

  <div class="abs reg">Registered in England and Wales, company number 01234567, VAT Number GB 9876543</div>
</footer>

<div class="abs bottom">
  <div class="legal">© 2015 ZEPPO wares. All Rights Reserved</div>
  <div class="social"><i></i><i></i><i></i><i></i></div>
</div>

</body>
</html>
```